Manufacturing company needs new business card.

I need a unique Business Card that will truly stand out. Nothing too busy. Simple is good, right? Not looking for a standard design either. No cookie cutter layout. I am just looking for something interesting and a bit different. Does't have to completely off the wall crazy, just not your run of the mill business card. Clean and modern with a touch of industrial.

Target Market(s)

Air conditioning industry, Architects, builders.

Industry/Entity Type

Business

Contact Information for Business Card

Details to be included on card are:

Peter Vance
Managing Director

T: 1300 847 519
M: 0428 593 174
W: www.brenvaleworks.com.au
E: peter.vance@brenvaleworks.com.au
A: 58 Harwick Lane, Sydney NSW 2000

Font styles to use
Sans Serif

Colors
0355a3
848484
fbfbfb

Requirements
Must have
• Card design must be landscape.

```html
<!DOCTYPE html>
<html lang="en">
<head>
<meta charset="utf-8">
<title>Brenvale Works – Business Card</title>
<link rel="stylesheet" href="https://fonts.googleapis.com/css2?family=Exo+2:wght@400;600;700&family=Open+Sans:wght@400;600&display=swap">
<style>
  :root {
    --brand-blue: #0355a3;
    --card-blue: #1f4fa6;
    --steel-grey: #848484;
    --paper: #fbfbfb;
    --ink-grey: #5a5a5a;
    --backdrop: #e6e7ea;
  }
  * { box-sizing: border-box; margin: 0; padding: 0; }
  html, body { width: 1200px; height: 892px; overflow: hidden; }
  body { background: var(--backdrop); position: relative; font-family: "Open Sans", sans-serif; }

  .card {
    position: absolute;
    top: 298px;
    width: 520px;
    height: 297px;
    overflow: hidden;
    box-shadow: 0 6px 18px rgba(0,0,0,0.18);
  }

  /* Front: contact side */
  .card-front { left: 50px; background: var(--card-blue); }
  .front-panel {
    position: absolute;
    left: 46px; top: 36px; right: 0; bottom: 42px;
    background: var(--paper);
  }
  .front-notch {
    position: absolute;
    right: 0; top: 36px;
    width: 70px; height: 62px;
    background: var(--steel-grey);
  }
  .front-notch-cut {
    position: absolute;
    right: 70px; top: 36px;
    width: 24px; height: 24px;
    background: var(--card-blue);
  }
  .holder-name {
    position: absolute; left: 170px; top: 54px;
    font-family: "Exo 2", sans-serif; font-weight: 700;
    font-size: 22px; letter-spacing: 1.5px;
    color: var(--brand-blue); text-transform: uppercase;
  }
  .holder-role {
    position: absolute; left: 170px; top: 84px;
    font-size: 13px; color: var(--ink-grey);
  }
  .front-brand {
    position: absolute; left: 68px; top: 138px;
    display: flex; flex-direction: column; align-items: flex-start; gap: 8px;
  }
  .front-brand .mark { width: 38px; height: 38px; background: var(--brand-blue); }
  .front-brand .brand-name {
    font-family: "Exo 2", sans-serif; font-weight: 600;
    font-size: 14px; color: var(--brand-blue); line-height: 1.1;
  }
  .divider {
    position: absolute; left: 178px; top: 128px;
    width: 1px; height: 112px; background: var(--steel-grey);
  }
  .contact-list {
    position: absolute; left: 192px; top: 128px;
    list-style: none; display: flex; flex-direction: column; gap: 8px;
  }
  .contact-list li {
    display: flex; align-items: center; gap: 9px;
    font-size: 12.5px; color: var(--ink-grey);
  }
  .contact-list svg { width: 14px; height: 14px; flex: none; fill: var(--brand-blue); }

  /* Back: brand side */
  .card-back { left: 630px; background: var(--card-blue); color: var(--paper); }
  .back-lockup {
    position: absolute; left: 52px; top: 98px;
    display: flex; align-items: center; gap: 18px;
  }
  .back-lockup .mark { width: 52px; height: 52px; background: var(--paper); }
  .back-wordmark { font-family: "Exo 2", sans-serif; }
  .back-wordmark .brand-name {
    font-weight: 600; font-size: 36px; line-height: 1; letter-spacing: 0.5px;
  }
  .back-wordmark .region {
    display: flex; align-items: center; gap: 10px; margin-top: 6px;
  }
  .back-wordmark .region .rule { width: 120px; height: 1px; background: var(--paper); }
  .back-wordmark .region span {
    font-size: 13px; letter-spacing: 10px; font-weight: 400;
  }
  .back-web {
    position: absolute; left: 52px; top: 186px;
    font-family: "Exo 2", sans-serif; font-size: 21px; letter-spacing: 1px;
  }
</style>
</head>
<body>

<section class="card card-front" aria-label="Business card front">
  <div class="front-panel"></div>
  <div class="front-notch-cut"></div>
  <div class="front-notch"></div>

  <h1 class="holder-name">Peter Vance</h1>
  <p class="holder-role">Managing Director</p>

  <div class="front-brand">
    <span class="mark"></span>
    <span class="brand-name">Brenvale<br>Works</span>
  </div>

  <div class="divider"></div>

  <ul class="contact-list">
    <li>
      <svg viewBox="0 0 16 16" aria-hidden="true"><path d="M3 2h3l1.5 3.5-2 1.2a8 8 0 0 0 3.8 3.8l1.2-2L14 10v3a1 1 0 0 1-1 1A11 11 0 0 1 2 3a1 1 0 0 1 1-1z"/></svg>
      1300 847 519
    </li>
    <li>
      <svg viewBox="0 0 16 16" aria-hidden="true"><path d="M5 1h6a1 1 0 0 1 1 1v12a1 1 0 0 1-1 1H5a1 1 0 0 1-1-1V2a1 1 0 0 1 1-1zm0 2v9h6V3zm3 10.2a.8.8 0 1 0 0-.01z"/></svg>
      0428 593 174
    </li>
    <li>
      <svg viewBox="0 0 16 16" aria-hidden="true"><path d="M8 1a7 7 0 1 0 3.5 13l-.6-1.2A5.6 5.6 0 1 1 13.6 8v.8c0 .8-.5 1.3-1.1 1.3s-1.1-.5-1.1-1.3V4.6h-1.3v.7A3.2 3.2 0 1 0 10.6 10a2.4 2.4 0 0 0 1.9 1c1.4 0 2.5-1 2.5-2.7V8A7 7 0 0 0 8 1zm0 4.9a2 2 0 1 1 0 4.1 2 2 0 0 1 0-4.1z"/></svg>
      peter.vance@brenvaleworks.com.au
    </li>
    <li>
      <svg viewBox="0 0 16 16" aria-hidden="true"><path d="M8 1a4.5 4.5 0 0 0-4.5 4.5C3.5 9 8 15 8 15s4.5-6 4.5-9.5A4.5 4.5 0 0 0 8 1zm0 6.3a1.8 1.8 0 1 1 0-3.6 1.8 1.8 0 0 1 0 3.6z"/></svg>
      58 Harwick Lane, Sydney NSW 2000
    </li>
  </ul>
</section>

<section class="card card-back" aria-label="Business card back">
  <div class="back-lockup">
    <span class="mark"></span>
    <div class="back-wordmark">
      <div class="brand-name">Brenvale Works</div>
      <div class="region"><span class="rule"></span><span>AUSTRALIA</span></div>
    </div>
  </div>
  <p class="back-web">www.brenvaleworks.com.au</p>
</section>

</body>
</html>
```